Business Card for Beach theme sports bar called TAVRU

I need a business card designed for our employees, front and back. This will be used by the employees of two business locations to hand out to customers. I've attached the previous business cards we used at one time for a Benwicks (it is now Tavru). Looking for a fresh new card that is elegant but has character.

Target Market(s)

30-60, middle class

Contact Information for Business Card

We are a beach bar and sports bar. I am looking for an elegant business card with the front to have the TAVRU logo. Then on the back I need it to allow a space for employees to write their names and for them to write in their schedule. I have attached our old cards with our old name Benwicks so you can pull everything we need on the cards. one thing is missing is we have another location at 2815 N Willow Crest Rd with a number of 702-418-9351. Since we will use it for both locations it should allow the employee to circle or check mark the bar which they work at.

Font styles to use
Sans Serif

Requirements
Must have
• We are looking for some fresh ideas for the business card. Something that will really stick out to customers when the staff hands them out. Creativity will be looked at positively, but we still want it to look upscale and fun.

```html
<!DOCTYPE html>
<html lang="en">
<head>
<meta charset="utf-8">
<title>TAVRU Business Cards</title>
<link href="https://fonts.googleapis.com/css2?family=Montserrat:wght@400;600;700;800&family=Great+Vibes&display=swap" rel="stylesheet">
<style>
  :root{
    --bg-center:#4a4a4a;
    --bg-edge:#141414;
    --card-black:#231f20;
    --card-white:#ffffff;
    --text-light:#f2f2f2;
    --text-muted:#9a9a9a;
    --yellow:#f7c314;
    --red:#e31b23;
    --green:#3bb54a;
    --grey:#8c8c8c;
    --orange:#f05a24;
    --tan:#c49a6c;
  }
  *{box-sizing:border-box;margin:0;padding:0}
  html,body{width:1200px;height:918px;overflow:hidden}
  body{
    background:radial-gradient(ellipse at center,var(--bg-center) 0%,var(--bg-edge) 100%);
    font-family:"Montserrat",Arial,sans-serif;
  }
  .variants{
    display:grid;
    grid-template-columns:repeat(3,400px);
    grid-template-rows:repeat(2,459px);
  }
  .variant{
    display:flex;flex-direction:column;align-items:center;
    gap:18px;padding-top:32px;
  }
  .variant--yellow{--accent:var(--yellow)}
  .variant--red{--accent:var(--red)}
  .variant--green{--accent:var(--green)}
  .variant--grey{--accent:var(--grey)}
  .variant--orange{--accent:var(--orange)}
  .variant--tan{--accent:var(--tan)}

  .card{
    position:relative;width:330px;height:189px;
    background:var(--card-black);overflow:hidden;
    box-shadow:0 6px 14px rgba(0,0,0,.55);
  }

  /* back side */
  .schedule{position:absolute;left:16px;top:16px;list-style:none}
  .schedule li{display:flex;align-items:center;gap:6px;height:16px;
    color:var(--text-light);font-size:9px;font-weight:700}
  .schedule .day-dot{width:9px;height:9px;border-radius:50%;background:var(--accent)}
  .offer{position:absolute;left:150px;top:14px;color:var(--accent);
    font-size:19px;font-weight:800;letter-spacing:.3px}
  .role{position:absolute;left:150px;top:42px;color:var(--text-light);
    font-size:13px;font-weight:700}
  .name-field{position:absolute;left:70px;top:68px;width:118px;height:58px;
    border-radius:10px;background:var(--accent)}
  .locations{position:absolute;left:200px;top:70px;list-style:none}
  .location{display:flex;gap:7px;margin-bottom:9px}
  .location-check{flex:none;width:9px;height:9px;margin-top:2px;border-radius:50%;background:var(--accent)}
  .location-text{color:var(--text-light);font-size:7px;line-height:9.5px;font-weight:600}
  .fine-print{position:absolute;left:16px;bottom:9px;right:16px;
    color:var(--text-muted);font-size:6.5px;line-height:9px;letter-spacing:.4px}

  /* front side */
  .front-art{position:absolute;inset:0}
  .brand{position:absolute;left:18px;top:76px;width:130px;
    display:flex;align-items:center;gap:7px}
  .brand-dot{width:12px;height:12px;border-radius:50%;background:var(--accent)}
  .brand-name{color:var(--card-black);font-size:28px;font-weight:800;letter-spacing:1px}
  .tagline{position:absolute;left:200px;top:36px;width:110px;text-align:center;
    font-family:"Great Vibes",cursive;color:var(--text-light);
    font-size:19px;line-height:38px}
</style>
</head>
<body>
<main class="variants">

  <section class="variant variant--yellow">
    <article class="card card--back">
      <ul class="schedule"><li><span class="day-dot"></span>M</li><li><span class="day-dot"></span>T</li><li><span class="day-dot"></span>W</li><li><span class="day-dot"></span>TH</li><li><span class="day-dot"></span>F</li><li><span class="day-dot"></span>SA</li><li><span class="day-dot"></span>SU</li></ul>
      <p class="offer">$20 MATCH PLAY</p>
      <p class="role">Bartender</p>
      <div class="name-field"></div>
      <ul class="locations">
        <li class="location"><span class="location-check"></span><span class="location-text">6140 W Harbor Palm Rd<br>Las Vegas, NV 89147<br>702-530-7724<br>cs@tavrubar.com</span></li>
        <li class="location"><span class="location-check"></span><span class="location-text">2815 N Willow Crest Rd<br>702-418-9351<br>cs@tavrubar.com</span></li>
      </ul>
      <p class="fine-print">Match play for new slot members, must play full amount.<br>Please see bartender for details. Management reserves rights.</p>
    </article>
    <article class="card card--front">
      <svg class="front-art" viewBox="0 0 330 189" aria-hidden="true"><path d="M0 0H150Q232 95 138 189H0Z" fill="#fff"/><path d="M150 0Q232 95 138 189" fill="none" stroke="var(--accent)" stroke-width="6"/><path d="M322 16H330V189H308Q324 120 322 16Z" fill="var(--accent)"/></svg>
      <div class="brand"><span class="brand-dot"></span><span class="brand-name">Tavru</span></div>
      <p class="tagline">A Beach Bar<br>&amp;<br>Sports Bar</p>
    </article>
  </section>

  <section class="variant variant--red">
    <article class="card card--back">
      <ul class="schedule"><li><span class="day-dot"></span>M</li><li><span class="day-dot"></span>T</li><li><span class="day-dot"></span>W</li><li><span class="day-dot"></span>TH</li><li><span class="day-dot"></span>F</li><li><span class="day-dot"></span>SA</li><li><span class="day-dot"></span>SU</li></ul>
      <p class="offer">$20 MATCH PLAY</p>
      <p class="role">Bartender</p>
      <div class="name-field"></div>
      <ul class="locations">
        <li class="location"><span class="location-check"></span><span class="location-text">6140 W Harbor Palm Rd<br>Las Vegas, NV 89147<br>702-530-7724<br>cs@tavrubar.com</span></li>
        <li class="location"><span class="location-check"></span><span class="location-text">2815 N Willow Crest Rd<br>702-418-9351<br>cs@tavrubar.com</span></li>
      </ul>
      <p class="fine-print">Match play for new slot members, must play full amount.<br>Please see bartender for details. Management reserves rights.</p>
    </article>
    <article class="card card--front">
      <svg class="front-art" viewBox="0 0 330 189" aria-hidden="true"><path d="M0 0H150Q232 95 138 189H0Z" fill="#fff"/><path d="M150 0Q232 95 138 189" fill="none" stroke="var(--accent)" stroke-width="6"/><path d="M322 16H330V189H308Q324 120 322 16Z" fill="var(--accent)"/></svg>
      <div class="brand"><span class="brand-dot"></span><span class="brand-name">Tavru</span></div>
      <p class="tagline">A Beach Bar<br>&amp;<br>Sports Bar</p>
    </article>
  </section>

  <section class="variant variant--green">
    <article class="card card--back">
      <ul class="schedule"><li><span class="day-dot"></span>M</li><li><span class="day-dot"></span>T</li><li><span class="day-dot"></span>W</li><li><span class="day-dot"></span>TH</li><li><span class="day-dot"></span>F</li><li><span class="day-dot"></span>SA</li><li><span class="day-dot"></span>SU</li></ul>
      <p class="offer">$20 MATCH PLAY</p>
      <p class="role">Bartender</p>
      <div class="name-field"></div>
      <ul class="locations">
        <li class="location"><span class="location-check"></span><span class="location-text">6140 W Harbor Palm Rd<br>Las Vegas, NV 89147<br>702-530-7724<br>cs@tavrubar.com</span></li>
        <li class="location"><span class="location-check"></span><span class="location-text">2815 N Willow Crest Rd<br>702-418-9351<br>cs@tavrubar.com</span></li>
      </ul>
      <p class="fine-print">Match play for new slot members, must play full amount.<br>Please see bartender for details. Management reserves rights.</p>
    </article>
    <article class="card card--front">
      <svg class="front-art" viewBox="0 0 330 189" aria-hidden="true"><path d="M0 0H150Q232 95 138 189H0Z" fill="#fff"/><path d="M150 0Q232 95 138 189" fill="none" stroke="var(--accent)" stroke-width="6"/><path d="M322 16H330V189H308Q324 120 322 16Z" fill="var(--accent)"/></svg>
      <div class="brand"><span class="brand-dot"></span><span class="brand-name">Tavru</span></div>
      <p class="tagline">A Beach Bar<br>&amp;<br>Sports Bar</p>
    </article>
  </section>

  <section class="variant variant--grey">
    <article class="card card--back">
      <ul class="schedule"><li><span class="day-dot"></span>M</li><li><span class="day-dot"></span>T</li><li><span class="day-dot"></span>W</li><li><span class="day-dot"></span>TH</li><li><span class="day-dot"></span>F</li><li><span class="day-dot"></span>SA</li><li><span class="day-dot"></span>SU</li></ul>
      <p class="offer">$20 MATCH PLAY</p>
      <p class="role">Bartender</p>
      <div class="name-field"></div>
      <ul class="locations">
        <li class="location"><span class="location-check"></span><span class="location-text">6140 W Harbor Palm Rd<br>Las Vegas, NV 89147<br>702-530-7724<br>cs@tavrubar.com</span></li>
        <li class="location"><span class="location-check"></span><span class="location-text">2815 N Willow Crest Rd<br>702-418-9351<br>cs@tavrubar.com</span></li>
      </ul>
      <p class="fine-print">Match play for new slot members, must play full amount.<br>Please see bartender for details. Management reserves rights.</p>
    </article>
    <article class="card card--front">
      <svg class="front-art" viewBox="0 0 330 189" aria-hidden="true"><path d="M0 0H150Q232 95 138 189H0Z" fill="#fff"/><path d="M150 0Q232 95 138 189" fill="none" stroke="var(--accent)" stroke-width="6"/><path d="M322 16H330V189H308Q324 120 322 16Z" fill="var(--accent)"/></svg>
      <div class="brand"><span class="brand-dot"></span><span class="brand-name">Tavru</span></div>
      <p class="tagline">A Beach Bar<br>&amp;<br>Sports Bar</p>
    </article>
  </section>

  <section class="variant variant--orange">
    <article class="card card--back">
      <ul class="schedule"><li><span class="day-dot"></span>M</li><li><span class="day-dot"></span>T</li><li><span class="day-dot"></span>W</li><li><span class="day-dot"></span>TH</li><li><span class="day-dot"></span>F</li><li><span class="day-dot"></span>SA</li><li><span class="day-dot"></span>SU</li></ul>
      <p class="offer">$20 MATCH PLAY</p>
      <p class="role">Bartender</p>
      <div class="name-field"></div>
      <ul class="locations">
        <li class="location"><span class="location-check"></span><span class="location-text">6140 W Harbor Palm Rd<br>Las Vegas, NV 89147<br>702-530-7724<br>cs@tavrubar.com</span></li>
        <li class="location"><span class="location-check"></span><span class="location-text">2815 N Willow Crest Rd<br>702-418-9351<br>cs@tavrubar.com</span></li>
      </ul>
      <p class="fine-print">Match play for new slot members, must play full amount.<br>Please see bartender for details. Management reserves rights.</p>
    </article>
    <article class="card card--front">
      <svg class="front-art" viewBox="0 0 330 189" aria-hidden="true"><path d="M0 0H150Q232 95 138 189H0Z" fill="#fff"/><path d="M150 0Q232 95 138 189" fill="none" stroke="var(--accent)" stroke-width="6"/><path d="M322 16H330V189H308Q324 120 322 16Z" fill="var(--accent)"/></svg>
      <div class="brand"><span class="brand-dot"></span><span class="brand-name">Tavru</span></div>
      <p class="tagline">A Beach Bar<br>&amp;<br>Sports Bar</p>
    </article>
  </section>

  <section class="variant variant--tan">
    <article class="card card--back">
      <ul class="schedule"><li><span class="day-dot"></span>M</li><li><span class="day-dot"></span>T</li><li><span class="day-dot"></span>W</li><li><span class="day-dot"></span>TH</li><li><span class="day-dot"></span>F</li><li><span class="day-dot"></span>SA</li><li><span class="day-dot"></span>SU</li></ul>
      <p class="offer">$20 MATCH PLAY</p>
      <p class="role">Bartender</p>
      <div class="name-field"></div>
      <ul class="locations">
        <li class="location"><span class="location-check"></span><span class="location-text">6140 W Harbor Palm Rd<br>Las Vegas, NV 89147<br>702-530-7724<br>cs@tavrubar.com</span></li>
        <li class="location"><span class="location-check"></span><span class="location-text">2815 N Willow Crest Rd<br>702-418-9351<br>cs@tavrubar.com</span></li>
      </ul>
      <p class="fine-print">Match play for new slot members, must play full amount.<br>Please see bartender for details. Management reserves rights.</p>
    </article>
    <article class="card card--front">
      <svg class="front-art" viewBox="0 0 330 189" aria-hidden="true"><path d="M0 0H150Q232 95 138 189H0Z" fill="#fff"/><path d="M150 0Q232 95 138 189" fill="none" stroke="var(--accent)" stroke-width="6"/><path d="M322 16H330V189H308Q324 120 322 16Z" fill="var(--accent)"/></svg>
      <div class="brand"><span class="brand-dot"></span><span class="brand-name">Tavru</span></div>
      <p class="tagline">A Beach Bar<br>&amp;<br>Sports Bar</p>
    </article>
  </section>

</main>
</body>
</html>
```